Business Card Design Project

HI! Can you design a business card with the logo you designed for me? I don't know what the typical order is so can you place it in the order most people do? White background and also play with a couple of colored backgrounds. Thank you!

Darnel Quesvo-Tranetti
darnel@tovenashcoaching.example
tovenashcoaching.example
555-317-4809

Target Market(s)

Women

Industry/Entity Type

Business

```html
<!DOCTYPE html>
<html lang="en">
<head>
<meta charset="utf-8">
<title>Tovenash Coaching Services — Business Card</title>
<link href="https://fonts.googleapis.com/css2?family=Josefin+Sans:wght@400;600;700&display=swap" rel="stylesheet">
<style>
  :root {
    --canvas-grey: #a9a9a9;
    --card-red: #c0141c;
    --card-red-deep: #8e0b10;
    --card-red-soft: #d42a2a;
    --accent-orange: #f58220;
    --panel-white: #ffffff;
    --brand-red: #b3121b;
    --text-white: #ffffff;
  }
  * { margin: 0; padding: 0; box-sizing: border-box; }
  html, body {
    width: 1200px;
    height: 1000px;
    overflow: hidden;
  }
  body {
    background: var(--canvas-grey);
    font-family: "Josefin Sans", sans-serif;
    position: relative;
  }
  .business-card {
    position: absolute;
    left: 350px;
    top: 62px;
    width: 500px;
    height: 875px;
    overflow: hidden;
    background: radial-gradient(ellipse at 50% 70%, var(--card-red-soft) 0%, var(--card-red) 45%, var(--card-red-deep) 100%);
  }
  .card-shapes {
    position: absolute;
    inset: 0;
    width: 100%;
    height: 100%;
  }
  .brand-block {
    position: absolute;
    left: 0;
    right: 0;
    top: 96px;
    text-align: center;
  }
  .brand-dot {
    display: block;
    width: 112px;
    height: 112px;
    margin: 0 auto 26px;
    border-radius: 50%;
    background: var(--accent-orange);
  }
  .brand-name {
    color: var(--brand-red);
    font-weight: 600;
    line-height: 1;
  }
  .brand-name .brand-main {
    display: block;
    font-size: 64px;
    letter-spacing: 1px;
  }
  .brand-name .brand-sub {
    display: block;
    margin-top: 14px;
    font-size: 25px;
    letter-spacing: 5px;
    text-transform: uppercase;
  }
  .contact-block {
    position: absolute;
    left: 0;
    right: 0;
    top: 566px;
    text-align: center;
    color: var(--text-white);
    text-shadow: 2px 3px 3px rgba(60, 0, 0, 0.55);
  }
  .contact-name {
    font-size: 36px;
    font-weight: 700;
    margin-bottom: 14px;
  }
  .contact-line {
    font-size: 25px;
    font-weight: 600;
    line-height: 1.5;
  }
  .contact-phone {
    font-size: 40px;
    font-weight: 700;
    margin-top: 6px;
    letter-spacing: 1px;
  }
</style>
</head>
<body>
  <main class="business-card">
    <svg class="card-shapes" viewBox="0 0 500 875" preserveAspectRatio="none" aria-hidden="true">
      <ellipse cx="250" cy="302" rx="380" ry="240" fill="var(--panel-white)" stroke="var(--accent-orange)" stroke-width="6"/>
      <ellipse cx="250" cy="1100" rx="420" ry="330" fill="var(--card-red-deep)" fill-opacity="0.35" stroke="var(--accent-orange)" stroke-width="6"/>
    </svg>

    <header class="brand-block">
      <span class="brand-dot"></span>
      <h1 class="brand-name">
        <span class="brand-main">Tovenash</span>
        <span class="brand-sub">Coaching Services</span>
      </h1>
    </header>

    <section class="contact-block">
      <p class="contact-name">Darnel Quesvo-Tranetti</p>
      <p class="contact-line">darnel@tovenashcoaching.example</p>
      <p class="contact-line">tovenashcoaching.example</p>
      <p class="contact-phone">555-317-4809</p>
    </section>
  </main>
</body>
</html>
```